Business Card Design Needed

Business car design required, logo will be supplied.

Brambleford Power Surveyors are looking to become the leading provider of energy performance certificates to estate agents, landlords and home owners in the Yorkshire region of the UK.

The business card must be double sided and professional looking. Estate agents receive hundreds of cards from contractors and our card must stand out.

I require a two sided business card that is clean, modern and created by a designer that can think outside of the box.

Brand colours can be supplied .

Please ask if you have any questions.

Target Market(s)

Estate agents, landlords and property owners

Industry/Entity Type

Property - estate agency - energy consultants

Contact Information for Business Card

Tomas Rendell - Energy Assessor - 07311642705 - www.BramblefordPSV.co.uk - info@bramblefordpsv.co.uk

Font styles to use
Serif
Sans Serif

Colors
00AB8E
00BBA5
67D7C9
C6EFE9
E9F9F6

Requirements
Must have
• Use the provided logo, clean, professional and stand out from the crowd
Nice to have
• Clever use of text, spacing and brand colours
Should not have
• Clip art

```html
<!DOCTYPE html>
<html lang="en">
<head>
<meta charset="utf-8">
<title>Brambleford Power Surveyors – Business Card</title>
<link href="https://fonts.googleapis.com/css2?family=Ubuntu:wght@300;400&display=swap" rel="stylesheet">
<style>
  :root {
    --backdrop: #1b6aa5;
    --brand-blue: #1e67a3;
    --brand-green: #c3d72f;
    --card-white: #fafbfd;
    --panel-tint: #f5f7fa;
    --text-grey: #545454;
    --edge-grey: #e7ebf2;
  }
  * { box-sizing: border-box; margin: 0; padding: 0; }
  html, body { width: 1200px; height: 900px; overflow: hidden; }
  body {
    background: var(--backdrop);
    font-family: "Ubuntu", sans-serif;
    position: relative;
  }
  .card {
    position: absolute;
    left: 273px;
    width: 654px;
    height: 374px;
    background: var(--card-white);
    overflow: hidden;
  }
  .card--front { top: 46px; }
  .card--back { top: 481px; }

  /* Front side */
  .brand-panel {
    position: absolute;
    left: 0; top: 0;
    width: 327px; height: 366px;
    background: var(--panel-tint);
    display: flex;
    flex-direction: column;
    align-items: center;
    justify-content: center;
    gap: 18px;
  }
  .brand-dot {
    width: 86px; height: 86px;
    border-radius: 50%;
    background: var(--brand-green);
  }
  .brand-name {
    color: var(--brand-blue);
    font-weight: 400;
    font-size: 24px;
    line-height: 1.15;
    text-align: center;
    letter-spacing: 0.5px;
  }
  .accent-bar {
    position: absolute;
    left: 0; bottom: 0;
    width: 327px; height: 8px;
    background: var(--brand-green);
  }
  .edge-strip {
    position: absolute;
    left: 327px; bottom: 0;
    right: 0; height: 8px;
    background: var(--edge-grey);
  }
  .person {
    position: absolute;
    left: 371px; top: 98px;
  }
  .person__name {
    color: var(--text-grey);
    font-size: 29px;
    font-weight: 400;
    letter-spacing: 0.3px;
  }
  .person__role {
    color: var(--brand-green);
    font-size: 15px;
    letter-spacing: 0.8px;
    margin-top: 3px;
    margin-left: 12px;
  }
  .contact {
    position: absolute;
    left: 371px;
    list-style: none;
    color: var(--text-grey);
    font-size: 16.5px;
    letter-spacing: 0.3px;
  }
  .contact li { display: flex; align-items: center; gap: 15px; }
  .contact svg { width: 14px; height: 14px; flex: none; }
  .contact--phone { top: 220px; }
  .contact--web { top: 266px; }
  .contact--web li + li { margin-top: 5px; }

  /* Back side */
  .back-lockup {
    position: absolute;
    left: 95px; top: 125px;
    display: flex;
    align-items: center;
    gap: 22px;
  }
  .back-lockup .brand-dot { width: 80px; height: 80px; }
  .divider {
    width: 1.5px; height: 85px;
    background: var(--brand-blue);
  }
  .back-lockup .brand-name {
    font-size: 33px;
    text-align: left;
    line-height: 1.1;
  }
  .wave-field {
    position: absolute;
    left: 0; top: 247px;
    width: 100%; height: 119px;
    background: linear-gradient(90deg, rgba(220,226,238,0.5) 0%, rgba(250,251,253,0) 45%, rgba(195,215,47,0.18) 80%, rgba(195,215,47,0.28) 100%);
  }
</style>
</head>
<body>

  <section class="card card--front">
    <div class="brand-panel">
      <div class="brand-dot"></div>
      <p class="brand-name">Brambleford<br>Power Surveyors</p>
    </div>
    <div class="accent-bar"></div>
    <div class="edge-strip"></div>

    <div class="person">
      <h1 class="person__name">Tomas Rendell</h1>
      <p class="person__role">ENERGY ASSESSOR</p>
    </div>

    <ul class="contact contact--phone">
      <li>
        <svg viewBox="0 0 16 16" aria-hidden="true"><path fill="var(--brand-green)" d="M3.6 1.5l2.2 2.7-1.3 1.6c.8 2 2.4 3.6 4.4 4.5l1.6-1.3 2.7 2.2-1.4 2.2C6.6 13.4 2.6 9.4 2.1 3.3z"/><path fill="none" stroke="var(--brand-green)" stroke-width="1.3" d="M9.5 3.2a4 4 0 0 1 3.3 3.3M9.6 .9a6.3 6.3 0 0 1 5.5 5.5"/></svg>
        <span>07311642705</span>
      </li>
    </ul>

    <ul class="contact contact--web">
      <li>
        <svg viewBox="0 0 16 16" aria-hidden="true"><rect x="1" y="3" width="14" height="10" fill="var(--brand-green)"/><path d="M1.5 3.5L8 9l6.5-5.5M1.5 12.5l5-4.5M14.5 12.5l-5-4.5" fill="none" stroke="#fff" stroke-width="1.1"/></svg>
        <span>info@bramblefordpsv.co.uk</span>
      </li>
      <li>
        <svg viewBox="0 0 16 16" aria-hidden="true"><g fill="none" stroke="var(--brand-green)" stroke-width="1.4"><circle cx="8" cy="8" r="6.5"/><ellipse cx="8" cy="8" rx="2.8" ry="6.5"/><path d="M1.5 8h13M2.5 4.8h11M2.5 11.2h11"/></g></svg>
        <span>www.BramblefordPSV.co.uk</span>
      </li>
    </ul>
  </section>

  <section class="card card--back">
    <div class="back-lockup">
      <div class="brand-dot"></div>
      <div class="divider"></div>
      <p class="brand-name">Brambleford<br>Power Surveyors</p>
    </div>
    <div class="wave-field" role="img" aria-label="Soft flowing line pattern in pale grey and lime green"></div>
    <div class="edge-strip" style="left:0"></div>
  </section>

</body>
</html>
```